Webpage Toggle Button Graphics

We are a webhosting company that sells Hosted Servers (Windows/Linux etc). We have for each service in our catalogue a number of on/off/maybe toggle buttons (not actally buttons, but display). Out current design is not modern enough, and would like a new design for the concept. (current screenshot is attached).
Updates

It seems I need to clarify something.  The ICONS I need are for the Buttons in the attachment marked Anti-virus, File Backup, HIDS, DR.  Not anything else on the page. The New icons do need to fit in with the look and feel of the page, and ideally are smaller (so we can fit more of these ICONS on the page). Thanks              

Industry/Entity Type

It Company

Requirements
Must have
• Generic Button Display, with 4 states- ON (Red/Bad, I have this feature), OFF (Green/Good, I do not have this feature), N/A (greyed out, feature is not available), MAYBE (Blue, I dont have this feature but its not really Red/Bad)
• Prefer a generic version with a single visual cue (dot/button or whatever) and a Text Description (i.e. not a custom ICON for each feature)
• Needs to fit in the space similiar to the screenshot, but Ideally smaller.
• Initial buttons are to be for:
• Anti-Virus (AV)
• Backup (Back)
• Host Intrusion Detection (HIDS)
• Disaster Recovery (DR)
• DDOS (DDOS)
• Can submittions be in the format of the attachment with your designs embedded into the picture to show what it will look like in production. May Icon 1-RED, 2, Green, 3 Blue, 4 - Greyed out.
Nice to have
• Ideally the button/display is generic, and our developers can just add the text for any future buttons

```html
<!DOCTYPE html>
<html lang="en">
<head>
<meta charset="utf-8">
<title>Service Feature Status Toggles</title>
<link rel="stylesheet" href="https://fonts.googleapis.com/css2?family=Source+Sans+3:wght@400;600&family=Arimo:wght@400;700&display=swap">
<style>
:root{
  --bg:#f4f4f4;
  --pill-top:#f7f7f7;
  --pill-bottom:#d9d9d9;
  --pill-border:#cfcfcf;
  --pill-text:#555;
  --dot-red:#e22b2b;
  --dot-green:#8cc63f;
  --dot-blue:#2b88d8;
  --dot-grey:#e8e8e8;
  --head-text:#555;
  --head-dark:#333;
  --row-alt:#eef2f7;
  --link:#1f5aa8;
  --body-text:#333;
  --rule:#c9ddef;
  --server-blue:#1d9ad9;
}
*{margin:0;padding:0;box-sizing:border-box}
html,body{width:1200px;height:588px;overflow:hidden}
body{
  position:relative;
  background:radial-gradient(ellipse 700px 320px at 600px 330px,#fff 40%,var(--bg) 100%);
  font-family:Arimo,Arial,sans-serif;
}
.big-pill{
  position:absolute;top:89px;height:58px;border-radius:11px;
  background:linear-gradient(#fbfbfb,var(--pill-bottom));
  border:1px solid var(--pill-border);
  box-shadow:inset 0 1px 0 #fff;
  font-family:"Source Sans 3",sans-serif;font-size:25px;color:var(--pill-text);
  display:flex;align-items:center;padding-left:64px;
}
.big-pill::after{
  content:"";position:absolute;left:2px;right:2px;top:58px;height:16px;border-radius:0 0 11px 11px;
  background:linear-gradient(rgba(210,210,210,.45),rgba(255,255,255,0));
}
.big-pill .dot{position:absolute;left:16px;top:17px;width:24px;height:24px;border-radius:50%}
.dot.red{background:radial-gradient(circle at 40% 35%,#ff7a7a,var(--dot-red) 60%,#b31212);border:2px solid #fff;box-shadow:0 0 0 1px #bbb}
.dot.green{background:radial-gradient(circle at 40% 35%,#c6ef86,var(--dot-green) 60%,#5d9a1e);border:2px solid #fff;box-shadow:0 0 0 1px #bbb}
.dot.blue{background:radial-gradient(circle at 40% 35%,#7cc2ff,var(--dot-blue) 60%,#175fa6);border:2px solid #fff;box-shadow:0 0 0 1px #bbb}
.dot.grey{background:radial-gradient(circle at 40% 35%,#fff,var(--dot-grey) 60%,#cfcfcf);border:2px solid #fff;box-shadow:0 0 0 1px #bbb}

.col-head{position:absolute;top:259px;font-size:13px;font-weight:700;color:var(--head-text)}
.col-head .sort{display:inline-block;width:13px;height:13px;border-radius:50%;border:1px solid #9bbbdd;background:#fff;vertical-align:-2px;margin-left:2px;position:relative}
.col-head .sort::after{content:"";position:absolute;left:3px;top:4px;border:3px solid transparent;border-top:4px solid var(--link)}
.col-head.dark{color:var(--head-dark)}
.col-head.faint{top:235px;color:#bbb}

.rule{position:absolute;width:1px;background:var(--rule)}
.row{position:absolute;left:79px;width:1040px}
.row.alt{background:var(--row-alt)}
.server-icon{position:absolute;left:7px;width:46px;height:46px;border-radius:4px;
  background:linear-gradient(#46c0f2,var(--server-blue) 55%,#1678b8);border:1px solid #1370aa}
.server-icon::after{content:"";position:absolute;left:17px;top:8px;width:12px;height:28px;background:#eaf6fd;border:1px solid #b7dff4}
.type{position:absolute;left:58px;font-size:14px;color:var(--body-text)}
.name{position:absolute;left:230px;font-size:14px;line-height:23px;color:var(--body-text)}
.name b{color:var(--link)}
.pill{position:absolute;width:102px;height:27px;border-radius:5px;
  background:linear-gradient(var(--pill-top),var(--pill-bottom));border:1px solid var(--pill-border);
  font-family:"Source Sans 3",sans-serif;font-size:12px;color:var(--pill-text);line-height:25px;padding-left:31px}
.pill i{position:absolute;left:9px;top:8px;width:9px;height:9px;border-radius:50%}
.pill i.red{background:var(--dot-red)}
.pill i.green{background:var(--dot-green)}
.pill i.blue{background:var(--dot-blue)}
.pill i.grey{background:#eee;border:1px solid #ccc}
.actions{position:absolute;left:930px;width:98px;height:28px;border:1px solid #cde;border-radius:3px;background:#fff;
  font-size:14px;color:#666;line-height:26px;padding-left:11px}
.actions::after{content:"";position:absolute;right:3px;top:5px;width:16px;height:16px;background:#eee;border:1px solid #ddd}
.actions::before{content:"";position:absolute;right:8px;top:12px;border:3px solid transparent;border-top:4px solid #999;z-index:1}
.fade-bottom{position:absolute;left:0;top:478px;width:1200px;height:110px;background:linear-gradient(rgba(250,250,250,.3),#f7f7f7 25%)}
.fade-right{position:absolute;left:1050px;top:230px;width:150px;height:280px;background:linear-gradient(90deg,rgba(250,250,250,0),rgba(248,248,248,.7) 40%,#f8f8f8 75%)}
</style>
</head>
<body>
<div class="big-pill" style="left:149px;width:208px"><span class="dot grey"></span>File Backup</div>
<div class="big-pill" style="left:378px;width:211px"><span class="dot green"></span>Anti-Virus</div>
<div class="big-pill" style="left:611px;width:210px"><span class="dot red"></span>Anti-Virus</div>
<div class="big-pill" style="left:842px;width:209px"><span class="dot blue"></span>DR</div>

<div class="col-head" style="left:81px">Service Type<span class="sort"></span></div>
<div class="col-head" style="left:309px">Service Name<span class="sort"></span></div>
<div class="col-head dark" style="left:591px">Settings<span class="sort"></span></div>
<div class="col-head faint" style="left:694px">Associated</div>
<div class="col-head dark" style="left:694px">Features<span class="sort"></span></div>
<div class="col-head dark" style="left:893px">Associated Features</div>

<div class="row alt" style="top:281px;height:74px">
  <div class="server-icon" style="top:14px"></div>
  <div class="type" style="top:18px">Virtual Managed Server</div>
  <div class="name" style="top:3px"><b>My New Virtual Managed Server<br>#134190</b><br>MIVMS7738042</div>
  <div class="pill" style="left:509px;top:15px"><i class="red"></i>Anti-Virus</div>
  <div class="pill" style="left:614px;top:15px"><i class="red"></i>File Backup</div>
  <div class="pill" style="left:719px;top:15px"><i class="red"></i>HIDS</div>
  <div class="pill" style="left:823px;top:15px"><i class="red"></i>DR</div>
  <div class="actions" style="top:15px">Actions</div>
</div>
<div class="row" style="top:355px;height:64px">
  <div class="server-icon" style="top:9px"></div>
  <div class="type" style="top:12px">Virtual Managed Server</div>
  <div class="name" style="top:8px"><b>Orvel_Linux_14_2</b><br>MIVMS7738035</div>
  <div class="pill" style="left:509px;top:15px"><i class="red"></i>Anti-Virus</div>
  <div class="pill" style="left:614px;top:15px"><i class="grey"></i>File Backup</div>
  <div class="pill" style="left:719px;top:15px"><i class="red"></i>HIDS</div>
  <div class="pill" style="left:823px;top:15px"><i class="blue"></i>DR</div>
  <div class="actions" style="top:16px">Actions</div>
</div>
<div class="row alt" style="top:419px;height:64px">
  <div class="server-icon" style="top:9px"></div>
  <div class="type" style="top:12px">Virtual Managed Server</div>
  <div class="name" style="top:8px"><b>Orvel_linux_14_1</b><br>MIVMS7738033</div>
  <div class="pill" style="left:509px;top:14px"><i class="green"></i>Anti-Virus</div>
  <div class="pill" style="left:614px;top:14px"><i class="red"></i>File Backup</div>
  <div class="pill" style="left:719px;top:14px"><i class="red"></i>HIDS</div>
  <div class="pill" style="left:823px;top:14px"><i class="red"></i>DR</div>
  <div class="actions" style="top:16px">Actions</div>
</div>
<div class="row" style="top:483px;height:40px">
  <div class="server-icon" style="top:8px"></div>
  <div class="type" style="top:12px">Dedicated Server</div>
  <div class="name" style="top:8px"><b>Dedicated Server</b></div>
</div>

<div class="rule" style="left:586px;top:240px;height:260px"></div>
<div class="rule" style="left:1006px;top:281px;height:219px"></div>
<div class="fade-right"></div>
<div class="fade-bottom"></div>
</body>
</html>
```